Owen's 1st Birthday Invite

My wife and I need an Invite that looks like a Basketball Game Ticket. I will upload some examples which are our inspiration. Would like Owen Photoshopped on Marco Vell on Harbor Ridge Game Ticket. Maybe use the "The Summit" Ticket that I uploaded as the Template. Replace with "The First Birthday" Alternative Design is the same concept with a Rangers Ticket. Big rangers fans! May even purchase both designs if given the chance. Party Date - 7/1/18 Location - Briarwood Lodge Winter Garden, FL (5192 Cedar Moss Ln, Winter Garden, FL 34787)

Target Market(s)

30 something parents.

Requirements
Must have
• Picture of my Son Owen. "Owenfield Marcus Hale" on flyer somewhere. RSVP @ owenmarcusparty.example
Nice to have
• Rangers mockup. Design with Owenfield as Cole Varnet on ticket.

```html
<!DOCTYPE html>
<html lang="en">
<head>
<meta charset="UTF-8">
<title>The First Birthday – Owenfield Marcus Hale</title>
<link rel="stylesheet" href="https://fonts.googleapis.com/css2?family=Kaushan+Script&family=Alfa+Slab+One&family=Arimo:wght@400;700&display=swap">
<style>
  :root {
    --gold-light: #fbe28a;
    --gold: #f3c640;
    --amber: #e7a93a;
    --ink: #1c2230;
    --black: #0c0c0c;
    --band: #fcc30b;
    --canvas: #ffffff;
  }
  html, body {
    margin: 0;
    padding: 0;
    overflow: hidden;
    background: var(--canvas);
  }
  .invite {
    position: relative;
    width: 831px;
    height: 1200px;
    overflow: hidden;
    background: var(--gold);
  }
  .backdrop {
    position: absolute;
    inset: 0;
    background:
      radial-gradient(ellipse at 62% 8%, #fff4c4 0%, rgba(255,244,196,0) 42%),
      radial-gradient(ellipse at 40% 48%, #f2c675 0%, rgba(242,198,117,0) 58%),
      linear-gradient(180deg, var(--gold-light) 0%, var(--gold) 45%, var(--amber) 100%);
  }
  .child-photo {
    position: absolute;
    left: 548px;
    top: 378px;
    width: 283px;
    height: 680px;
    border-radius: 140px 140px 0 0;
    background:
      radial-gradient(ellipse at 50% 30%, #b98062 0%, #8a5a43 20%, rgba(138,90,67,0) 34%),
      linear-gradient(180deg, #efe9e4 0%, #ebe6e1 50%, #4d5360 72%, #d58a3a 88%, #c8782f 100%);
  }
  .title-small, .title-large, .blessing {
    position: absolute;
    margin: 0;
    font-family: "Kaushan Script", cursive;
    color: var(--ink);
    font-weight: 400;
    line-height: 1;
  }
  .title-small { left: 106px; top: 66px; font-size: 72px; }
  .title-large { left: 118px; top: 150px; font-size: 168px; letter-spacing: -2px; }
  .blessing { left: 93px; top: 555px; font-size: 60px; }
  .name {
    position: absolute;
    left: 36px;
    margin: 0;
    font-family: "Alfa Slab One", serif;
    color: var(--black);
    line-height: 1;
    transform-origin: left top;
    text-shadow:
      3px 3px 0 var(--gold-light),
      -1px -1px 0 var(--gold-light),
      5px 5px 4px rgba(0,0,0,0.35);
  }
  .name-first { top: 640px; font-size: 86px; transform: scaleY(1.3); }
  .name-middle { top: 770px; font-size: 96px; letter-spacing: 2px; transform: scaleY(1.05); }
  .name-last { top: 858px; left: 60px; font-size: 150px; letter-spacing: 6px; transform: scaleY(1.05); }
  .ticket-band {
    position: absolute;
    left: 0;
    top: 1054px;
    width: 831px;
    height: 94px;
    background: var(--band);
    border-top: 4px solid var(--black);
    border-bottom: 4px solid var(--black);
    box-sizing: border-box;
    display: flex;
    align-items: center;
  }
  .ticket-notch {
    position: absolute;
    top: 50%;
    width: 34px;
    height: 34px;
    margin-top: -17px;
    border-radius: 50%;
    background: var(--amber);
    border: 4px solid var(--black);
    box-sizing: border-box;
  }
  .ticket-notch.left { left: -17px; }
  .ticket-notch.right { right: -17px; }
  .ticket-perforation {
    position: absolute;
    top: 10px;
    bottom: 10px;
    left: 640px;
    border-left: 3px dashed var(--black);
  }
  .date-text {
    margin: 0 0 0 78px;
    font-family: "Arimo", sans-serif;
    font-size: 36px;
    color: var(--black);
  }
  .stub-text {
    position: absolute;
    left: 650px;
    right: 20px;
    margin: 0;
    text-align: center;
    font-family: "Arimo", sans-serif;
    font-weight: 700;
    font-size: 22px;
    line-height: 1.15;
    color: var(--black);
  }
  .party-details {
    position: absolute;
    left: 0;
    right: 0;
    top: 1152px;
    margin: 0;
    text-align: center;
    font-family: "Arimo", sans-serif;
    font-size: 17px;
    line-height: 22px;
    color: var(--black);
  }
  .party-details strong { font-weight: 700; }
</style>
</head>
<body>
  <main class="invite">
    <div class="backdrop" role="img" aria-label="Warm golden bokeh background with a soft, faded close-up portrait of the birthday child"></div>
    <div class="child-photo" role="img" aria-label="Photo of Owenfield sitting, wearing a white knit hat and a white long-sleeve shirt"></div>

    <h1 class="title-small">The First</h1>
    <p class="title-large">Birthday</p>

    <p class="blessing">Bless Me</p>
    <p class="name name-first">Owenfield</p>
    <p class="name name-middle">Marcus</p>
    <p class="name name-last">HALE</p>

    <div class="ticket-band">
      <span class="ticket-notch left"></span>
      <p class="date-text">Sunday, 1st of July, 2018</p>
      <span class="ticket-perforation"></span>
      <p class="stub-text">ADMIT<br>ONE</p>
      <span class="ticket-notch right"></span>
    </div>

    <p class="party-details"><strong>Briarwood Lodge</strong> · 5192 Cedar Moss Ln, Winter Garden, FL 34787<br><strong>RSVP</strong> @ owenmarcusparty.example</p>
  </main>
</body>
</html>
```